Social media design templates

A variety of templates incorporating our logo and colours to use for our postings on different social media platforms. Must be user friendly and meet our brand image. We have attached our logo to view. We would like some of the templates to offer the ability to insert a background image and others to be a template designed around our logo.

We are black and white in colour, and our values speak to our transparency and honesty, so we are looking for clean cut, sharp straight lines, not using any other colours or curved lines.

We are a recruitment company that will be using these templates
- job posting,
- general announcements,
- blog,
- company newsletter,
- updates,
- testimonials and
- top candidate profiles

We would like a gallery of templates to choose from to use separately that all represent our brand.

```html
<!DOCTYPE html>
<html lang="en">
<head>
<meta charset="utf-8">
<title>Announcement – Welcome</title>
<link rel="stylesheet" href="https://fonts.googleapis.com/css2?family=Roboto+Slab:wght@400;600&family=Poppins:wght@500&display=swap">
<style>
  :root {
    --ink-deep: #0c0c0c;
    --ink-mid: #161616;
    --ink-soft: #222222;
    --frame-line: rgba(255, 255, 255, 0.28);
    --text-white: #ffffff;
    --text-grey: #8f8f8f;
    --prop-light: #e4e4e4;
    --prop-dark: #7a7a7a;
  }
  * { margin: 0; padding: 0; box-sizing: border-box; }
  html, body { width: 1200px; height: 1200px; overflow: hidden; background: var(--ink-deep); }
  .post {
    position: relative;
    width: 1200px;
    height: 1200px;
    overflow: hidden;
    color: var(--text-white);
  }
  .post__backdrop {
    position: absolute;
    inset: 0;
    background:
      radial-gradient(ellipse at 65% 45%, var(--ink-soft) 0%, transparent 55%),
      linear-gradient(180deg, var(--ink-mid) 0%, var(--ink-deep) 55%, var(--ink-mid) 100%);
  }
  .post__frame {
    position: absolute;
    left: 223px;
    top: 159px;
    width: 754px;
    height: 811px;
    border: 1.5px solid var(--frame-line);
    background: rgba(255, 255, 255, 0.02);
  }
  .post__megaphone {
    position: absolute;
    left: 131px;
    top: 211px;
    width: 270px;
    height: 278px;
    background: linear-gradient(135deg, var(--prop-light) 0%, var(--prop-dark) 100%);
    opacity: 0.85;
  }
  .brand {
    position: absolute;
    left: 0;
    width: 1210px;
    top: 318px;
    display: flex;
    align-items: center;
    justify-content: center;
    gap: 12px;
    font-family: "Roboto Slab", serif;
    font-weight: 400;
    font-size: 20px;
    letter-spacing: 1px;
    text-transform: uppercase;
    color: var(--text-white);
  }
  .brand__mark {
    width: 14px;
    height: 14px;
    border: 1.5px solid var(--text-white);
  }
  .headline {
    position: absolute;
    left: 0;
    width: 1206px;
    text-align: center;
    font-family: "Roboto Slab", serif;
  }
  .headline__kicker {
    top: 510px;
    font-weight: 400;
    font-size: 44px;
    color: var(--text-grey);
    width: 1166px;
  }
  .headline__title {
    top: 570px;
    font-weight: 600;
    font-size: 104px;
    letter-spacing: 1px;
    line-height: 1.05;
    color: var(--text-white);
  }
  .post__body {
    position: absolute;
    left: 280px;
    width: 640px;
    top: 732px;
    text-align: center;
    font-family: "Poppins", sans-serif;
    font-weight: 500;
    font-size: 20px;
    line-height: 40px;
  }
  .post__contact {
    position: absolute;
    left: 0;
    width: 1200px;
    top: 1090px;
    text-align: center;
    font-family: "Poppins", sans-serif;
    font-weight: 500;
    font-size: 20px;
  }
</style>
</head>
<body>
  <main class="post">
    <div class="post__backdrop" role="img" aria-label="Dark night city skyline with blurred towers"></div>
    <div class="post__frame"></div>
    <div class="post__megaphone" role="img" aria-label="Illustration of a white and grey megaphone with small sound marks"></div>

    <div class="brand"><span class="brand__mark"></span>Hirebridge Group</div>

    <p class="headline headline__kicker">Announcement</p>
    <h1 class="headline headline__title">WELCOME</h1>

    <p class="post__body">Contrary to popular belief, Lorem Ipsum is not simply random<br>text. It has roots in a piece of classical Latin</p>

    <p class="post__contact">Contac us at hello@hirebridge.example</p>
  </main>
</body>
</html>
```